Successful Commercial Refrigeration business needs a flyer

We need a flyer (DL size) designed for our existing commercial refrigeration business. We are a family owned business, run by a father and son. We have been in operation since 1980 with the majority of our clients being based in Melbourne's South Eastern suburbs and we are now looking to get new clients in Melbourne's west.

Website can be accessed here http://coldhavenfridge.com.au/ to get further information on services we provide. Our main competitor is http://www.vortexchillworks.com.au/

Contact details are to be Trevor Hale, 0438 261 947, coldhaventh@mailbox.example
Updates

Hi All The majority of designs coming through are using images that have been pulled from the website. I'm happy for images to be use on the design (and just as happy for images not to be used) but I would prefer the images to be of front end equipment rather than backend (for instance, instead of showing the system thats on the roof, perhaps use a nice image of a bar or a cake fridge or something along those lines). We don't own these photos (they're from a competitor) but just wanted to give examples http://www.vortexchillworks.com.au/files/4013/7051/8196/IMG_2273.jpg http://www.vortexchillworks.com.au/files/3513/7051/8018/IMG_2267.JPG

Industry/Entity Type

Business

Requirements
Must have
• Contact details
Trevor Hale, 0438 261 947, coldhaventh@mailbox.example, www.coldhavenfridge.com.au

- services (info on websites listed in brief)

- refer to commercial refrigeration (not just refrigeration as we don't want domestic enquiries)

If there is going to be a call out regarding the area we service - please word it around "servicing all of melbourne"
my original brief explained that we were trying to build business in the western suburbs but now I realise that if we use that specific call out it will limit where we can send these flyers. So let's keep it generic.

```html
<!DOCTYPE html>
<html lang="en">
<head>
<meta charset="utf-8">
<title>Coldhaven Refrigeration – Flyer</title>
<link href="https://fonts.googleapis.com/css2?family=Montserrat:wght@700;800;900&display=swap" rel="stylesheet">
<style>
  :root {
    --sky: #83a8d8;
    --navy: #1b2a4a;
    --ink: #000000;
    --paper: #ffffff;
    --alert: #e3161b;
    --map-land: #e6e4b6;
    --map-sea: #8fb6d9;
  }
  * { margin: 0; padding: 0; box-sizing: border-box; }
  html, body { width: 1200px; height: 2547px; overflow: hidden; background: var(--paper); }
  .flyer {
    position: relative; width: 1200px; height: 2547px; overflow: hidden;
    background: var(--sky);
    font-family: "Montserrat", Arial, sans-serif;
  }
  .hero-photo {
    position: absolute; left: 0; top: 0; width: 1200px; height: 820px;
    background:
      linear-gradient(180deg, rgba(131,168,216,0) 55%, var(--sky) 100%),
      linear-gradient(90deg, #dfe9f2 0%, #7fb6e6 18%, #2f79c9 40%, #5aa2e0 60%, #9fd0f0 80%, #3b86d0 100%);
  }
  .service-map {
    position: absolute; left: 742px; top: 1019px; width: 385px; height: 461px;
    border: 12px solid var(--ink); border-radius: 30px;
    background: linear-gradient(180deg, var(--map-land) 0%, var(--map-land) 55%, var(--map-sea) 100%);
  }
  .shapes { position: absolute; left: 0; top: 0; }
  .brand-name {
    position: absolute; left: 85px; top: 590px; width: 1060px;
    color: var(--paper); font-weight: 900; text-transform: uppercase;
    font-size: 150px; line-height: 142px; letter-spacing: -2px;
  }
  .brand-name span { display: block; font-size: 120px; line-height: 122px; }
  .credentials {
    position: absolute; left: 85px; top: 900px; width: 1040px;
    display: flex; justify-content: space-between;
    font-weight: 800; font-size: 34px; color: var(--ink);
  }
  .area-callout {
    position: absolute; left: 148px; top: 1098px; width: 440px;
    text-align: center; color: var(--paper); font-weight: 900;
    font-size: 60px; line-height: 68px; transform: rotate(-6deg);
  }
  .services-headline {
    position: absolute; right: 82px; top: 1650px; width: 1040px;
    text-align: right; color: var(--paper); font-weight: 800;
    font-size: 45px; line-height: 62px;
  }
  .services-body {
    position: absolute; left: 140px; top: 1885px; width: 980px;
    color: var(--navy); font-weight: 800; font-size: 39px; line-height: 52px;
  }
  .contact {
    position: absolute; right: 59px; top: 2222px;
    text-align: right; color: var(--paper); font-weight: 800; font-style: normal;
    font-size: 45px; line-height: 65px;
  }
</style>
</head>
<body>
<main class="flyer">
  <div class="hero-photo" role="img" aria-label="Photo of a supermarket aisle lined with illuminated glass-door commercial display fridges"></div>

  <div class="service-map" role="img" aria-label="Map of greater Melbourne and Port Phillip Bay with a marker on the service location"></div>

  <svg class="shapes" width="1200" height="2547" viewBox="0 0 1200 2547" aria-hidden="true">
    <defs>
      <polygon id="spike" points="0,-283 -42,-228 42,-228"/>
    </defs>
    <polygon class="pointer" points="509,1160 538,1274 945,1234" fill="var(--alert)"/>
    <g class="starburst" transform="translate(368 1231)" fill="var(--ink)">
      <circle r="236"/>
      <use href="#spike"/><use href="#spike" transform="rotate(16.36)"/>
      <use href="#spike" transform="rotate(32.73)"/><use href="#spike" transform="rotate(49.09)"/>
      <use href="#spike" transform="rotate(65.45)"/><use href="#spike" transform="rotate(81.82)"/>
      <use href="#spike" transform="rotate(98.18)"/><use href="#spike" transform="rotate(114.55)"/>
      <use href="#spike" transform="rotate(130.91)"/><use href="#spike" transform="rotate(147.27)"/>
      <use href="#spike" transform="rotate(163.64)"/><use href="#spike" transform="rotate(180)"/>
      <use href="#spike" transform="rotate(196.36)"/><use href="#spike" transform="rotate(212.73)"/>
      <use href="#spike" transform="rotate(229.09)"/><use href="#spike" transform="rotate(245.45)"/>
      <use href="#spike" transform="rotate(261.82)"/><use href="#spike" transform="rotate(278.18)"/>
      <use href="#spike" transform="rotate(294.55)"/><use href="#spike" transform="rotate(310.91)"/>
      <use href="#spike" transform="rotate(327.27)"/><use href="#spike" transform="rotate(343.64)"/>
    </g>
    <path class="footer-highlight" d="M0 2165 C400 2150 900 2060 1200 1980 V2547 H0Z" fill="var(--paper)"/>
    <path class="footer-band" d="M0 2225 C400 2210 900 2140 1200 2065 V2547 H0Z" fill="var(--ink)"/>
  </svg>

  <h1 class="brand-name">Coldhaven<span>Refrigeration</span></h1>

  <div class="credentials">
    <span>FULLY LICENSED</span>
    <span>PTY LTD</span>
    <span>Est.1980</span>
  </div>

  <p class="area-callout">SERVICING<br>ALL OF<br>MELBOURNE<br>METRO</p>

  <h2 class="services-headline">ALL COMMERCIAL REFRIGERATION<br>AND DOMESTIC AND COMMERCIAL<br>AIR CONDITIONING</h2>

  <p class="services-body">For all your fridge, freezer, cool room,<br>bottle cabinets and air conditioner needs<br>please enquire today.</p>

  <address class="contact">
    Contact Trevor Hale<br>
    Phone 0438 261 947<br>
    Email coldhaventh@mailbox.example<br>
    Web www.coldhavenfridge.com.au
  </address>
</main>
</body>
</html>
```